Solvane Glow LED - E- Commerce site

We need a website designed for an LED Billboard company that sells:
1) LED Billboards (Sales & Rental)
2) LED Gas Station lights
3) Truss Systems (Sales & Rental)
4) Sound Systems (Sales & Rental)

Attached are websites that sell similar products as Solvane Glow LED. Target market is for business, property managers and event coordinators.
This site will need to be an e-commerce site where customers can purchase the product directly from the site. What I'm looking for is a design layout to start.

Conceptual Web Designs:
http://example-panelora.test/index.html
http://www.vormpix.com/
http://www.droneplayaudio.com/
http://www.quillmarkdisplay.com/

Attached is the logo of the company: Please note that the new spelling of the logo is "Solvane Glow LED" using domain " SolvaneGlowLED.com

Industry/Entity Type

Gas Station

Number of Pages Required

5+ page

Requirements
Must have
• 1) E-Commerce - Customers will need to be able to order product from the site.
• 2) Customers will also have the option to rent the product as well.
Nice to have
• I like the image of the attached website, that has a video clip loop
• http://www.quillmarkdisplay.com/

```html
<!DOCTYPE html>
<html lang="en">
<head>
<meta charset="utf-8">
<title>Solvane Glow LED</title>
<link href="https://fonts.googleapis.com/css2?family=Lato:wght@400;700&family=Open+Sans:wght@400;600;700&display=swap" rel="stylesheet">
<style>
:root{
  --pink:#e5157c;
  --black:#0b0b0b;
  --gold:#f5b800;
  --red:#e0262b;
  --amber:#e3a400;
  --grey-band:#ececec;
  --card-bar:#e8e8e8;
  --text:#222;
  --muted:#a6a6a6;
  --white:#fff;
}
*{box-sizing:border-box;margin:0;padding:0}
html,body{width:1200px;height:2862px;overflow:hidden}
body{position:relative;font-family:"Open Sans",Arial,sans-serif;color:var(--text);background:var(--white)}
.abs{position:absolute}
svg{display:block}

/* top bar */
.topbar{left:0;top:0;width:1200px;height:37px;background:var(--pink)}
.topbar-links{position:absolute;right:150px;top:0;height:37px;display:flex;gap:36px;align-items:center}
.topbar-links a{color:var(--white);font-size:11px;font-weight:700;text-decoration:none;display:flex;align-items:center;gap:8px;letter-spacing:.3px}

/* header */
.header{left:0;top:37px;width:1200px;height:98px;background:linear-gradient(#222,#111)}
.brand{position:absolute;left:130px;top:25px;display:flex;align-items:center;gap:12px}
.brand-dot{width:44px;height:44px;border-radius:50%;background:var(--gold)}
.brand-name{font-family:"Lato",sans-serif;font-weight:700;font-size:24px;color:var(--gold);line-height:1}
.search{position:absolute;left:576px;top:30px;width:200px;height:36px;border:1px solid #888;border-radius:18px;display:flex;align-items:center;padding:0 14px;justify-content:space-between}
.search span{color:#999;font-size:12px}
.phone{position:absolute;left:792px;top:28px;display:flex;align-items:center;gap:9px;color:var(--white);font-weight:700;font-size:15px}
.phone-ring{width:38px;height:38px;border:2px solid var(--white);border-radius:50%;display:flex;align-items:center;justify-content:center}
.cart{position:absolute;left:952px;top:32px;display:flex;gap:10px;color:var(--white)}
.cart b{font-size:10px;display:block}
.cart small{font-size:11px;color:#ccc}

/* hero */
.hero{left:0;top:135px;width:1200px;height:466px;background:linear-gradient(100deg,#3b2a1e 0%,#6b4a2a 22%,#a67a44 40%,#6a5a52 52%,#2a2a2a 60%,#c9a57e 78%,#8c6a4e 100%)}
.nav{left:82px;top:137px;width:1034px;height:42px;background:var(--white);border-radius:21px;display:flex;align-items:center;overflow:hidden;box-shadow:0 1px 3px rgba(0,0,0,.3)}
.nav a{font-family:"Lato",sans-serif;font-size:15px;color:#222;text-decoration:none;height:42px;line-height:42px;padding:0 26px;border-right:1px solid #ddd}
.nav a:last-child{border-right:none}
.nav a.active{background:var(--gold);font-weight:700;padding:0 30px 0 46px}
.hero-caption{left:0;top:337px;width:445px;height:115px;background:rgba(225,225,225,.75);clip-path:polygon(0 0,100% 0,92% 100%,0 100%)}
.hero-caption h1{font-family:"Lato",sans-serif;font-weight:700;font-size:38px;line-height:56px;color:#1a1a1a;padding:2px 0 0 130px}
.dots{left:572px;top:552px;display:flex;gap:7px}
.dots i{width:10px;height:10px;border-radius:50%;background:var(--white)}
.dots i:first-child{background:var(--pink)}

/* section headings */
.sec-title{left:0;width:1200px;text-align:center;font-family:"Lato",sans-serif;font-weight:700;font-size:34px;color:#111}
.divider{left:490px;width:220px;height:1px;background:#ccc}
.divider::after{content:"";position:absolute;left:106px;top:-4px;width:8px;height:8px;border-radius:50%;background:#bbb}

.about-text{left:164px;top:730px;width:872px;text-align:center;font-size:14.5px;line-height:25px;color:#222}

/* category grid */
.cats{left:131px;top:807px;width:936px;height:432px;display:grid;grid-template-columns:1fr 1fr;grid-template-rows:1fr 1fr;gap:4px;background:#111;padding:2px}
.cat{display:flex;align-items:center;justify-content:center;font-family:"Open Sans",sans-serif;font-weight:600;font-size:30px;color:var(--white);border:1px dashed rgba(255,255,255,.5)}
.cat-billboards{background:linear-gradient(160deg,#1b2a44,#4a5a7a 50%,#262636)}
.cat-gas{background:linear-gradient(180deg,#0c0c0c 20%,#6d6f73 45%,#c9ccd0 70%,#1a1a1a)}
.cat-truss{background:linear-gradient(150deg,#1a0f2e,#5a2a8a 50%,#2a1a4e)}
.cat-sound{background:linear-gradient(170deg,#3a3a44,#7a6e64 55%,#c9a88a)}

/* products */
.band-grey{left:0;width:1200px;background:var(--grey-band)}
.card{position:absolute;width:264px;height:320px;background:var(--white);border:1px solid #ddd;border-radius:8px;box-shadow:0 1px 4px rgba(0,0,0,.12);overflow:hidden}
.card-img{height:168px}
.card-title{height:32px;line-height:32px;background:var(--card-bar);text-align:center;font-weight:700;font-size:14px;color:#111}
.card-desc{text-align:center;font-size:12px;line-height:17px;color:var(--muted);padding:14px 24px 0}
.card-actions{display:flex;justify-content:center;gap:12px;margin-top:18px}
.btn{width:96px;height:28px;line-height:28px;text-align:center;color:var(--white);font-size:12px;font-weight:700}
.btn-buy{background:var(--red)}
.btn-rent{background:var(--amber)}
.img-round{background:radial-gradient(ellipse at center,#f4f4f4 0%,#d8d8d8 45%,#fff 70%)}
.img-tube{background:linear-gradient(160deg,#fff 25%,#e6e8ea 40%,#fff 55%,#e6e8ea 70%,#fff)}
.img-par{background:radial-gradient(circle at center,#3a3a3a 0%,#6a6a6a 30%,#fff 55%)}
.img-deck{background:radial-gradient(ellipse at center,#2a2a2a 0%,#555 35%,#fff 62%)}
.img-panel{background:radial-gradient(ellipse at center,#fafafa 0%,#d4d4d4 40%,#fff 65%)}
.img-t5{background:linear-gradient(165deg,#fff 30%,#e2e4e6 45%,#fff 60%)}

/* features */
.feature{position:absolute;top:2351px;width:302px;height:122px;background:var(--white);border-top:5px solid var(--pink);border-radius:6px;box-shadow:0 1px 4px rgba(0,0,0,.15);padding:12px 16px}
.feature h3{font-family:"Open Sans",sans-serif;font-weight:700;font-size:17px;color:#111}
.feature h4{font-size:12px;font-weight:600;margin-top:8px;color:#222}
.feature p{font-size:12px;line-height:18px;color:#333;margin-top:2px;width:220px}
.feature svg{position:absolute;right:16px;top:14px}

/* footer */
.footer{left:0;top:2510px;width:1200px;height:352px;background:var(--black)}
.f-brand{left:139px;top:2540px;display:flex;align-items:center;gap:12px}
.f-about{left:139px;top:2625px;width:350px;font-size:14px;line-height:24px;color:var(--white)}
.f-head{font-family:"Lato",sans-serif;font-weight:700;font-size:20px;color:var(--white)}
.f-links{list-style:none;font-size:13px;line-height:23px;color:var(--white)}
.f-links li::before{content:"›";color:var(--pink);margin-right:8px;font-weight:700}
.f-contact{font-size:13px;line-height:19px;color:var(--white)}
.f-contact li{list-style:none;display:flex;gap:12px;margin-bottom:14px}
.f-contact svg{flex:none;margin-top:2px}
.social{display:flex;flex-direction:column;gap:14px}
.social i{width:34px;height:34px;border:2px solid var(--pink);border-radius:50%}
.copy{left:132px;top:2827px;font-size:12px;color:var(--white)}
.payments{left:784px;top:2826px;display:flex;gap:7px}
.payments i{width:32px;height:20px;border-radius:2px;background:#e3e3e3}
.payments i:nth-child(3n+2){background:#3a6fc4}
.payments i:nth-child(3n){background:#9a9ad8}
</style>
</head>
<body>

<div class="abs topbar">
  <nav class="topbar-links">
    <a href="#"><svg width="12" height="12" viewBox="0 0 12 12"><circle cx="6" cy="3.5" r="3" fill="#fff"/><path d="M0 12c0-4 3-5 6-5s6 1 6 5z" fill="#fff"/></svg>MY ACCOUNT</a>
    <a href="#"><svg width="14" height="12" viewBox="0 0 14 12"><rect x="0" y="1" width="14" height="10" rx="1" fill="#fff"/></svg>MY WISHLIST</a>
    <a href="#"><svg width="14" height="12" viewBox="0 0 14 12"><rect x="0" y="1" width="14" height="10" rx="1" fill="none" stroke="#fff" stroke-width="1.6"/><line x1="0" y1="4" x2="14" y2="4" stroke="#fff" stroke-width="1.6"/></svg>CHECKOUT</a>
    <a href="#"><svg width="11" height="13" viewBox="0 0 11 13"><rect x="0" y="5" width="11" height="8" rx="1" fill="#fff"/><path d="M2.5 5V3.5a3 3 0 0 1 6 0V5" fill="none" stroke="#fff" stroke-width="1.6"/></svg>LOG IN / REGISTER</a>
  </nav>
</div>

<header class="abs header">
  <div class="brand"><span class="brand-dot"></span><span class="brand-name">Solvane Glow LED</span></div>
  <div class="search"><span>Search</span>
    <svg width="14" height="14" viewBox="0 0 14 14"><circle cx="6" cy="6" r="4.5" fill="none" stroke="#fff" stroke-width="2"/><line x1="9.5" y1="9.5" x2="13" y2="13" stroke="#fff" stroke-width="2"/></svg>
  </div>
  <div class="phone"><span class="phone-ring"><svg width="17" height="17" viewBox="0 0 24 24"><path d="M6.6 10.8a15 15 0 0 0 6.6 6.6l2.2-2.2a1 1 0 0 1 1-.25 11.4 11.4 0 0 0 3.6.57 1 1 0 0 1 1 1V20a1 1 0 0 1-1 1A17 17 0 0 1 3 4a1 1 0 0 1 1-1h3.5a1 1 0 0 1 1 1c0 1.25.2 2.45.57 3.57a1 1 0 0 1-.25 1z" fill="#fff"/></svg></span>123-456-7890</div>
  <div class="cart">
    <svg width="26" height="30" viewBox="0 0 26 30"><path d="M3 9h20l-2 20H5z" fill="#fff"/><path d="M8 9V6a5 5 0 0 1 10 0v3" fill="none" stroke="#fff" stroke-width="2"/></svg>
    <div><b>SHOPPING CART</b><small>0 item(s) ⌄</small></div>
  </div>
</header>

<section class="abs hero" role="img" aria-label="Night street with light trails beside a bus shelter holding an illuminated advertising lightbox"></section>
<nav class="abs nav">
  <a href="#" class="active">Home</a>
  <a href="#">LED lights&nbsp; Systems</a>
  <a href="#">Truss Systems</a>
  <a href="#">Sound Systems</a>
  <a href="#">Service and Support</a>
  <a href="#">About</a>
  <a href="#">Contact US</a>
</nav>
<div class="abs hero-caption"><h1>Light Up Your<br>Advertisement</h1></div>
<div class="abs dots"><i></i><i></i><i></i><i></i></div>

<h2 class="abs sec-title" style="top:636px">About Us</h2>
<div class="abs divider" style="top:704px"></div>
<p class="abs about-text">Lorem ipsum dolor sit amet, consectetuer adipiscing elit, sed diam nonummy nibh euismod tincidunt ut laoreet dolore magna aliquam erat volutpat. Ut wisi enim ad minim veniam, quis nostrud exerci tation ullamcorper suscipit lobortis nisl ut aliquip ex ea.</p>

<div class="abs cats">
  <a class="cat cat-billboards" role="img" aria-label="City street lined with LED billboards at night">LED Billboards</a>
  <a class="cat cat-gas" role="img" aria-label="Gas station canopy lit with LED lights">LED Gas Station Lights</a>
  <a class="cat cat-truss" role="img" aria-label="Stage truss structure under purple lighting">Truss Systems</a>
  <a class="cat cat-sound" role="img" aria-label="Hand adjusting a sound mixing console">Sound Systems</a>
</div>

<div class="abs band-grey" style="top:1286px;height:533px"></div>
<h2 class="abs sec-title" style="top:1312px;font-size:31px">Popular Products</h2>
<div class="abs divider" style="top:1376px"></div>

<article class="card" style="left:161px;top:1406px">
  <div class="card-img img-round" role="img" aria-label="Round recessed LED panel light"></div>
  <div class="card-title">30W-LED Panel Light</div>
  <p class="card-desc">Pellentesque in rhoncus? In nec cursus et, magna odio? Enim, magnis,</p>
  <div class="card-actions"><span class="btn btn-buy">Buy Now</span><span class="btn btn-rent">On Rent</span></div>
</article>
<article class="card" style="left:468px;top:1406px">
  <div class="card-img img-tube" role="img" aria-label="Two LED tube lights"></div>
  <div class="card-title">20W-T8-LED Tube-UL</div>
  <p class="card-desc">Pellentesque in rhoncus? In nec cursus et, magna odio? Enim, magnis,</p>
  <div class="card-actions"><span class="btn btn-buy">Buy Now</span><span class="btn btn-rent">On Rent</span></div>
</article>
<article class="card" style="left:775px;top:1406px">
  <div class="card-img img-par" role="img" aria-label="Stage spotlight fixture with barn doors"></div>
  <div class="card-title">DJ Truss arch</div>
  <p class="card-desc">Pellentesque in rhoncus? In nec cursus et, magna odio? Enim, magnis,</p>
  <div class="card-actions"><span class="btn btn-buy">Buy Now</span><span class="btn btn-rent">On Rent</span></div>
</article>

<h2 class="abs sec-title" style="top:1850px;font-size:31px">Latest Products</h2>
<div class="abs divider" style="top:1914px"></div>

<article class="card" style="left:161px;top:1946px">
  <div class="card-img img-deck" role="img" aria-label="DJ controller deck"></div>
  <div class="card-title">Pulsetrack DeckFour</div>
  <p class="card-desc">Pellentesque in rhoncus? In nec cursus et, magna odio? Enim, magnis,</p>
  <div class="card-actions"><span class="btn btn-buy">Buy Now</span><span class="btn btn-rent">On Rent</span></div>
</article>
<article class="card" style="left:468px;top:1946px">
  <div class="card-img img-panel" role="img" aria-label="Square LED panel light"></div>
  <div class="card-title">30W-LED Panel Light</div>
  <p class="card-desc">Pellentesque in rhoncus? In nec cursus et, magna odio? Enim, magnis,</p>
  <div class="card-actions"><span class="btn btn-buy">Buy Now</span><span class="btn btn-rent">On Rent</span></div>
</article>
<article class="card" style="left:775px;top:1946px">
  <div class="card-img img-t5" role="img" aria-label="Slim T5 LED batten light"></div>
  <div class="card-title">Lumenrail T5 LED</div>
  <p class="card-desc">Pellentesque in rhoncus? In nec cursus et, magna odio? Enim, magnis,</p>
  <div class="card-actions"><span class="btn btn-buy">Buy Now</span><span class="btn btn-rent">On Rent</span></div>
</article>

<div class="abs band-grey" style="top:2320px;height:190px;background:#d9d9d9"></div>
<div class="feature" style="left:125px">
  <h3>Free Home shipping!</h3>
  <h4>This is a snappy sub-title</h4>
  <p>Lorem ipsum dolor sit amet, consectetur adipisicing. Neque beatae.</p>
  <svg width="66" height="44" viewBox="0 0 66 44"><rect x="0" y="6" width="40" height="26" rx="3" fill="#e32b2b"/><path d="M40 14h14l10 10v8H40z" fill="#e32b2b"/><circle cx="14" cy="36" r="6" fill="#e32b2b"/><circle cx="52" cy="36" r="6" fill="#e32b2b"/><circle cx="14" cy="36" r="2.5" fill="#fff"/><circle cx="52" cy="36" r="2.5" fill="#fff"/></svg>
</div>
<div class="feature" style="left:444px">
  <h3>We're now global!</h3>
  <h4>This is a snappy sub-title</h4>
  <p>Lorem ipsum dolor sit amet, consectetur adipisicing. Neque beatae.</p>
  <svg width="50" height="50" viewBox="0 0 50 50"><circle cx="25" cy="25" r="21" fill="none" stroke="#e32b2b" stroke-width="3"/><ellipse cx="25" cy="25" rx="9" ry="21" fill="none" stroke="#e32b2b" stroke-width="2.5"/><line x1="4" y1="25" x2="46" y2="25" stroke="#e32b2b" stroke-width="2.5"/><line x1="8" y1="14" x2="42" y2="14" stroke="#e32b2b" stroke-width="2"/><line x1="8" y1="36" x2="42" y2="36" stroke="#e32b2b" stroke-width="2"/></svg>
</div>
<div class="feature" style="left:762px">
  <h3>Lowest price guarantee!</h3>
  <h4>This is a snappy sub-title</h4>
  <p>Lorem ipsum dolor sit amet, consectetur adipisicing. Neque beatae.</p>
  <svg width="46" height="60" viewBox="0 0 46 60"><path d="M14 2h30v34L26 58 4 36V14z" fill="#e32b2b" transform="rotate(18 23 30)"/><circle cx="28" cy="14" r="3.5" fill="#fff"/></svg>
</div>

<footer class="abs footer"></footer>
<div class="abs f-brand"><span class="brand-dot"></span><span class="brand-name">Solvane Glow LED</span></div>
<p class="abs f-about">Lorem ipsum dolor sit amet, consectetuer&nbsp; elit, sed diam nonummy nibh euismod tincidunt ut laoreet dolore magna aliquam erat volutpat. Ut wisi enim ad minim veniam, quis nostrud exerci tation ullamcorper suscipit lobortis nisl ut aliquip ex ea commodo</p>

<h3 class="abs f-head" style="left:515px;top:2552px">Useful Links</h3>
<ul class="abs f-links" style="left:518px;top:2600px">
  <li>Home</li><li>LED lights&nbsp; Systems</li><li>Truss Systems</li><li>Sound Systems</li><li>Service and Support</li><li>About</li><li>Contact US</li>
</ul>

<h3 class="abs f-head" style="left:713px;top:2552px">Contact</h3>
<ul class="abs f-contact" style="left:713px;top:2604px;width:210px">
  <li><svg width="12" height="16" viewBox="0 0 12 16"><path d="M6 0a6 6 0 0 1 6 6c0 4-6 10-6 10S0 10 0 6a6 6 0 0 1 6-6z" fill="#e5157c"/><circle cx="6" cy="6" r="2.2" fill="#000"/></svg><span>123, Lorem ipsum dolor sit nil amet, consectetur adipiscingt.</span></li>
  <li><svg width="14" height="14" viewBox="0 0 24 24"><path d="M6.6 10.8a15 15 0 0 0 6.6 6.6l2.2-2.2a1 1 0 0 1 1-.25 11.4 11.4 0 0 0 3.6.57 1 1 0 0 1 1 1V20a1 1 0 0 1-1 1A17 17 0 0 1 3 4a1 1 0 0 1 1-1h3.5a1 1 0 0 1 1 1c0 1.25.2 2.45.57 3.57a1 1 0 0 1-.25 1z" fill="#e5157c"/></svg><span>123-456-7890</span></li>
  <li><svg width="14" height="14" viewBox="0 0 14 14"><rect x="0" y="4" width="14" height="9" rx="1" fill="#e5157c"/><rect x="3" y="0" width="8" height="5" fill="#e5157c"/></svg><span>123-456-7890</span></li>
  <li><svg width="14" height="12" viewBox="0 0 14 12"><rect x="0" y="1" width="14" height="10" rx="1" fill="#e5157c"/><path d="M0 2l7 5 7-5" fill="none" stroke="#000" stroke-width="1.3"/></svg><span>info@solvaneglowled.test</span></li>
</ul>

<h3 class="abs f-head" style="left:967px;top:2552px">Follow Us</h3>
<div class="abs social" style="left:1002px;top:2605px"><i></i><i></i><i></i><i></i></div>

<p class="abs copy">Copyright © 2016 - Solvane Glow LED. All Rights Reserved</p>
<div class="abs payments"><i></i><i></i><i></i><i></i><i></i><i></i><i></i></div>

</body>
</html>
```